We are an integrated facilities management company.

We aggregate everything related to facilities maintenance. Repair-replacement of equipment and facility space materials from:
Asset gathering and tracking.
Vendor screening, contracting and management.
Service requirement development.
Work order processing and management.
Invoice reconciliation.
Vendor payment.
Reporting.
Capital equipment bids and project management.

Target Market(s)

Retail, hospitality, multi-family housing, long term healthcare.

Industry/Entity Type

Maintenance

Contact Information for Business Card

Professional and bold look. (see logo zip file)

Colors
3377b5
85abd2
cedeed

Requirements
Must have
• N/A
Nice to have
• N/A
Should not have
• N/A

```html
<!DOCTYPE html>
<html lang="en">
<head>
<meta charset="utf-8">
<title>Stewardline Facility Partners – Business Card</title>
<link rel="stylesheet" href="https://fonts.googleapis.com/css2?family=Open+Sans:ital,wght@0,400;0,700;1,400&display=swap">
<style>
  :root {
    --brand-blue: #0a56a3;
    --accent-blue: #85abd2;
    --pale-blue: #cedeed;
    --ink-grey: #555a60;
    --card-white: #ffffff;
    --backdrop: #6d6f72;
  }
  * { box-sizing: border-box; margin: 0; padding: 0; }
  html, body {
    width: 1200px; height: 1125px; overflow: hidden;
    background: var(--backdrop);
    font-family: "Open Sans", Arial, sans-serif;
  }
  .sheet {
    width: 1200px; height: 1125px;
    display: flex; flex-direction: column; align-items: center;
    justify-content: center; gap: 36px;
  }
  .card {
    width: 900px; height: 500px;
    box-shadow: 0 6px 18px rgba(0,0,0,.35);
    position: relative;
  }
  /* Front */
  .card--front {
    background: var(--brand-blue);
    display: flex; align-items: center; justify-content: center;
  }
  .brand { display: flex; align-items: center; gap: 26px; }
  .brand__square { width: 74px; height: 74px; background: var(--card-white); }
  .brand__text { color: var(--card-white); font-weight: 700; }
  .brand__name { font-size: 58px; line-height: 1; letter-spacing: 1px; }
  .brand__sub { font-size: 27px; line-height: 1.2; letter-spacing: 1px; margin-top: 4px; }
  .brand__tagline {
    font-weight: 400; font-size: 15px; letter-spacing: 4px;
    color: var(--pale-blue); margin-top: 6px; text-transform: uppercase;
  }
  /* Back */
  .card--back {
    background: var(--card-white);
    display: flex; align-items: center; justify-content: center;
  }
  .person { text-align: right; padding-right: 34px; }
  .person__name { color: var(--brand-blue); font-weight: 700; font-size: 32px; letter-spacing: .5px; }
  .person__role { color: var(--ink-grey); font-size: 24px; font-style: italic; margin-top: 2px; }
  .divider { width: 2px; height: 150px; background: var(--brand-blue); }
  .contact { padding-left: 30px; color: var(--ink-grey); font-size: 23px; line-height: 1.3; }
  .contact__address { margin-bottom: 6px; }
  .contact__row { display: flex; align-items: center; gap: 10px; }
  .contact__icon { width: 18px; height: 18px; fill: var(--brand-blue); flex: none; }
</style>
</head>
<body>
<main class="sheet">
  <section class="card card--front" aria-label="Card front">
    <div class="brand">
      <div class="brand__square"></div>
      <div class="brand__text">
        <div class="brand__name">STEWARDLINE</div>
        <div class="brand__sub">FACILITY PARTNERS</div>
        <div class="brand__tagline">Maintain · Repair · Replace</div>
      </div>
    </div>
  </section>

  <section class="card card--back" aria-label="Card back">
    <div class="person">
      <div class="person__name">DANIEL HARROW</div>
      <div class="person__role">President</div>
    </div>
    <div class="divider"></div>
    <div class="contact">
      <div class="contact__address">1820 Harborview Lane<br>Seacliff CA 92601</div>
      <div class="contact__row">
        <svg class="contact__icon" viewBox="0 0 24 24"><path d="M6.6 10.8a15 15 0 0 0 6.6 6.6l2.2-2.2c.3-.3.7-.4 1-.2 1.1.4 2.3.6 3.6.6.6 0 1 .4 1 1V20c0 .6-.4 1-1 1A17 17 0 0 1 3 4c0-.6.4-1 1-1h3.5c.6 0 1 .4 1 1 0 1.3.2 2.5.6 3.6.1.3 0 .7-.2 1z"/></svg>
        <span>555-318-0472</span>
      </div>
      <div class="contact__row">
        <svg class="contact__icon" viewBox="0 0 24 24"><path d="M2 5h20v2l-10 6L2 7z"/><path d="M2 9l10 6 10-6v10H2z"/></svg>
        <span>hello@stewardline.com</span>
      </div>
      <div class="contact__row">
        <svg class="contact__icon" viewBox="0 0 24 24"><circle cx="12" cy="12" r="10"/><path d="M2 12h20M12 2c3 3 3 17 0 20M12 2c-3 3-3 17 0 20" stroke="#fff" stroke-width="1.5" fill="none"/></svg>
        <span>www.stewardline.com</span>
      </div>
    </div>
  </section>
</main>
</body>
</html>
```